Business IT Services Billboard to attract local small businesses

We are Brivolane, a premier Managed Service Provider (MSP) specializing in comprehensive IT services and VOIP phone solutions exclusively for businesses. Our goal is to create a dynamic and visually engaging billboard advertisement that not only highlights our cutting-edge IT solutions but also emphasizes our state-of-the-art VOIP phone services. This billboard should communicate our commitment to providing innovative, reliable, and holistic technology solutions.
Target Market(s)
small business
Industry/Entity Type
Information Technology
Colors
Designer to choose colors to be used in the design.
Look and feel
Each slider illustrates characteristics of the customer's brand and the style your logo design should communicate.

```html
<!DOCTYPE html>
<html lang="en">
<head>
<meta charset="utf-8">
<title>Brivolane Billboard</title>
<link href="https://fonts.googleapis.com/css2?family=Exo+2:ital,wght@0,400;0,500;0,700;0,800;1,800;1,900&display=swap" rel="stylesheet">
<style>
  :root {
    --navy: #0f1c2e;
    --navy-deep: #0a1422;
    --blue: #1a7ccb;
    --blue-bright: #1f8ad9;
    --paper: #f1f2f4;
    --paper-shade: #dcdfe3;
    --ink: #0f1c2e;
    --white: #ffffff;
    --stage: #e9edf2;
  }
  * { margin: 0; padding: 0; box-sizing: border-box; }
  html, body { width: 1200px; height: 720px; overflow: hidden; }
  body {
    background: var(--stage);
    font-family: "Exo 2", sans-serif;
    position: relative;
  }
  .billboard {
    position: absolute;
    left: 20px; top: 90px;
    width: 1160px; height: 540px;
    background: var(--navy);
    overflow: hidden;
  }
  .message-panel {
    position: absolute;
    left: 0; top: 0;
    width: 545px; height: 450px;
    background: linear-gradient(160deg, var(--white) 0%, var(--paper) 60%, var(--paper-shade) 100%);
    padding: 48px 40px 0 48px;
  }
  .page-curl {
    position: absolute;
    left: 470px; top: 0;
    width: 110px; height: 450px;
  }
  .headline {
    font-style: italic;
    text-transform: uppercase;
    line-height: 0.98;
  }
  .headline-lead {
    display: block;
    color: var(--ink);
    font-weight: 800;
    font-size: 52px;
  }
  .headline-focus {
    display: block;
    color: var(--blue);
    font-weight: 900;
    font-size: 64px;
    line-height: 0.96;
  }
  .tagline {
    margin-top: 22px;
    color: var(--ink);
    font-weight: 500;
    font-size: 23px;
    line-height: 1.25;
    text-align: center;
    width: 420px;
  }
  .brand-panel {
    position: absolute;
    left: 545px; top: 0;
    width: 615px; height: 450px;
  }
  .brand-name {
    position: absolute;
    right: 48px; top: 34px;
    color: var(--blue-bright);
    font-weight: 800;
    font-size: 60px;
    letter-spacing: 3px;
    text-transform: uppercase;
  }
  .service-photo {
    position: absolute;
    left: 0; top: 120px;
    width: 615px; height: 330px;
    background: radial-gradient(ellipse at 30% 45%, #e8f2fb 0%, #8fb2d2 30%, #3d5f82 65%, #1c2f47 100%);
  }
  .call-bar {
    position: absolute;
    left: 0; bottom: 0;
    width: 545px; height: 90px;
    background: var(--navy-deep);
    display: flex;
    align-items: center;
    padding-left: 48px;
    color: var(--white);
    font-weight: 500;
    font-size: 34px;
  }
  .web-bar {
    position: absolute;
    right: 0; bottom: 0;
    width: 615px; height: 90px;
    background: var(--blue);
    display: flex;
    align-items: center;
    gap: 20px;
    padding-left: 60px;
    color: var(--white);
    font-weight: 700;
    font-size: 40px;
  }
  .globe-icon { width: 40px; height: 40px; flex: none; }
</style>
</head>
<body>
  <main class="billboard">
    <section class="message-panel">
      <h1 class="headline">
        <span class="headline-lead">Elevate Your</span>
        <span class="headline-lead">Business With</span>
        <span class="headline-focus">Next-Gen</span>
        <span class="headline-focus">IT and VOIP</span>
        <span class="headline-focus">Services</span>
      </h1>
      <p class="tagline">Innovative IT and VOIP Solutions<br>Tailored for Your Business Success</p>
    </section>

    <svg class="page-curl" viewBox="0 0 110 450" aria-hidden="true">
      <defs>
        <linearGradient id="curlShade" x1="0" x2="1" y1="0" y2="0">
          <stop offset="0" stop-color="#ffffff"/>
          <stop offset="0.6" stop-color="#d4d8dd"/>
          <stop offset="1" stop-color="#9aa2ab"/>
        </linearGradient>
      </defs>
      <path d="M75 0 L110 0 L110 450 L0 450 C40 420 55 380 60 300 C65 200 70 80 75 0 Z" fill="url(#curlShade)"/>
    </svg>

    <section class="brand-panel">
      <div class="brand-name">Brivolane</div>
      <div class="service-photo" role="img" aria-label="Office headset resting on a desk beside a desk phone, with glowing cloud network icons overlaid"></div>
    </section>

    <div class="call-bar">Transform Your Tech Today at</div>
    <div class="web-bar">
      <svg class="globe-icon" viewBox="0 0 40 40" aria-hidden="true" fill="none" stroke="#0f1c2e" stroke-width="3">
        <circle cx="20" cy="20" r="17"/>
        <ellipse cx="20" cy="20" rx="7" ry="17"/>
        <line x1="3" y1="20" x2="37" y2="20"/>
        <line x1="6" y1="11" x2="34" y2="11"/>
        <line x1="6" y1="29" x2="34" y2="29"/>
      </svg>
      <span>www.brivolane.com</span>
    </div>
  </main>
</body>
</html>
```